Jackpot Display Wallpaper Design

We develop Jackpot Systems for Casinos and have a web based Jackpot Odometer display. Our software works by superimposing dynamic content over a fixed background.

We require the design of a fixed background of dimensions 1920 x 1080 incorporating higher quality graphical design work and creative ideas.

See File 4 below - "High Hand TEMPLATE". The finished work will resemble this image, with the grey background replaced with your creative design. The black panels will be replaced with your panels, with nice borders and interior shading or pattern. Our software will dynamically superimpose content over the panels. The panels should be of similar size and location to those shown although this is not strictly rigid and you can relocate or resize panels to a limited extent.

The end result when our software runs is something like File 5 below - "High Hand SAMPLE RESULT". Note that the example shows a patterned blue background, a red logo area, and grey shading within the panels.

The text within the panels is rendered dynamically by our application.

** This is a very plain design and only intended to illustrate how we superimpose text and playing cards onto a background. Do not take any design cues from this image.

Please provide the background, and blank panels. The panels can (and should) have some texture or shading that will look good when we render text over them.

Feel free to suggest a font and/or text color that you think would look good against your background and we can render the content in the font / color you suggest.

Target Market(s)

Poker Room facilities and Casinos

Industry/Entity Type

Software

Font styles to use
Sans Serif

Requirements
Must have
• - A graphic design based on the template called High Hand TEMPLATE.
• - 1920 x 1080 Photoshop image using separate layers.
• - The design needs to be edgy and reflect gaming, casinos and poker rooms.
Nice to have
• -Please see files 1, 2, and 3 below by way of "edgy" style guide.
• - For files 1, 2, 3 - ignore the "Bad Beat" wording but focus on the design style by way of example.
• - The background may or may not include the words "Poker" and / or "Jackpot"
• - You can fill in the panels with some sample content to illustrate how it will look.
• - The area at bottom containing scrolling text may be a frame with a border or just an area where we superimpose the scrolling text.

```html
<!DOCTYPE html>
<html lang="en">
<head>
<meta charset="utf-8">
<title>Jackpot Display Background</title>
<link rel="stylesheet" href="https://fonts.googleapis.com/css2?family=Bowlby+One&display=swap">
<style>
  :root {
    --felt-dark: #062a0a;
    --felt: #0d5c16;
    --felt-bright: #1c8f22;
    --glow: #55ff3c;
    --gold: #e0a21a;
    --gold-light: #fff6b0;
    --gold-deep: #a86a05;
    --panel-top: #0c0000;
    --panel-mid: #3a0000;
    --panel-red: #7a0000;
    --panel-red-dark: #2a0000;
    --band: #021a05;
    --burst-pale: #cdeee6;
    --burst-yellow: #f0e65a;
    --burst-orange: #c97a12;
    --burst-green: #7fbf3a;
  }
  html, body {
    margin: 0;
    padding: 0;
    width: 1200px;
    height: 675px;
    overflow: hidden;
    background: var(--felt-dark);
  }
  .stage {
    position: relative;
    width: 1200px;
    height: 675px;
    overflow: hidden;
    background:
      radial-gradient(ellipse 560px 360px at 600px 260px, var(--felt-bright) 0%, var(--felt) 50%, var(--felt-dark) 100%);
  }
  .panel-glow {
    position: absolute;
    left: 240px; top: 70px;
    width: 720px; height: 580px;
    background: radial-gradient(ellipse at center, rgba(85,255,60,0.5) 0%, rgba(85,255,60,0.15) 45%, rgba(85,255,60,0) 70%);
  }
  .title-glow {
    position: absolute;
    left: 180px; top: 250px;
    width: 840px; height: 200px;
    background: radial-gradient(ellipse 50% 50% at center, rgba(255,240,110,0.95) 0%, rgba(240,200,40,0.7) 35%, rgba(160,200,40,0.25) 65%, rgba(0,0,0,0) 100%);
  }
  .star-burst {
    position: absolute;
    top: 0;
    width: 400px;
    height: 675px;
  }
  .star-burst--left {
    left: 0;
    background:
      radial-gradient(circle 70px at 80px 60px, var(--burst-pale) 0%, rgba(205,238,230,0) 100%),
      radial-gradient(circle 80px at 90px 190px, var(--burst-pale) 0%, rgba(205,238,230,0) 100%),
      radial-gradient(circle 75px at 90px 330px, var(--burst-pale) 0%, rgba(205,238,230,0) 100%),
      radial-gradient(circle 75px at 140px 470px, var(--burst-pale) 0%, rgba(205,238,230,0) 100%),
      radial-gradient(circle 75px at 80px 580px, var(--burst-pale) 0%, rgba(205,238,230,0) 100%),
      radial-gradient(circle 55px at 240px 110px, var(--burst-pale) 0%, rgba(205,238,230,0) 100%),
      radial-gradient(circle 55px at 240px 380px, var(--burst-pale) 0%, rgba(205,238,230,0) 100%),
      radial-gradient(ellipse 260px 320px at 330px 330px, rgba(240,230,90,0.9) 0%, rgba(201,122,18,0.7) 45%, rgba(127,191,58,0) 100%),
      linear-gradient(180deg, rgba(127,191,58,0.6) 0%, rgba(201,122,18,0.5) 50%, rgba(127,191,58,0.4) 100%);
    -webkit-mask-image: linear-gradient(90deg, #000 0%, #000 70%, rgba(0,0,0,0) 100%);
    mask-image: linear-gradient(90deg, #000 0%, #000 70%, rgba(0,0,0,0) 100%);
  }
  .star-burst--right {
    right: 0;
    background:
      radial-gradient(circle 70px at 320px 60px, var(--burst-pale) 0%, rgba(205,238,230,0) 100%),
      radial-gradient(circle 80px at 310px 180px, var(--burst-pale) 0%, rgba(205,238,230,0) 100%),
      radial-gradient(circle 75px at 320px 300px, var(--burst-pale) 0%, rgba(205,238,230,0) 100%),
      radial-gradient(circle 75px at 260px 380px, var(--burst-pale) 0%, rgba(205,238,230,0) 100%),
      radial-gradient(circle 75px at 320px 560px, var(--burst-pale) 0%, rgba(205,238,230,0) 100%),
      radial-gradient(circle 55px at 160px 100px, var(--burst-pale) 0%, rgba(205,238,230,0) 100%),
      radial-gradient(circle 55px at 160px 360px, var(--burst-pale) 0%, rgba(205,238,230,0) 100%),
      radial-gradient(ellipse 260px 320px at 70px 330px, rgba(240,230,90,0.9) 0%, rgba(201,122,18,0.7) 45%, rgba(127,191,58,0) 100%),
      linear-gradient(180deg, rgba(127,191,58,0.6) 0%, rgba(201,122,18,0.5) 50%, rgba(127,191,58,0.4) 100%);
    -webkit-mask-image: linear-gradient(270deg, #000 0%, #000 70%, rgba(0,0,0,0) 100%);
    mask-image: linear-gradient(270deg, #000 0%, #000 70%, rgba(0,0,0,0) 100%);
  }
  .panel {
    position: absolute;
    box-sizing: border-box;
    border: 2px solid var(--gold);
    box-shadow: 0 0 0 1px var(--gold-deep), inset 0 0 0 1px rgba(255,220,120,0.35);
  }
  .panel--title-tab {
    left: 340px; top: 118px; width: 522px; height: 46px;
    border-radius: 8px 8px 0 0;
    background: #000;
  }
  .panel--main {
    left: 166px; top: 157px; width: 872px; height: 169px;
    border-radius: 10px;
    background: linear-gradient(180deg, var(--panel-top) 0%, var(--panel-mid) 100%);
  }
  .panel--detail-tab {
    left: 342px; top: 390px; width: 520px; height: 42px;
    border-radius: 8px 8px 0 0;
    background: linear-gradient(180deg, var(--panel-red) 0%, #6a0000 100%);
  }
  .panel--detail {
    left: 130px; top: 426px; width: 942px; height: 168px;
    border-radius: 10px;
    background: linear-gradient(180deg, var(--panel-red) 0%, var(--panel-red) 55%, var(--panel-red-dark) 100%);
  }
  .panel__divider {
    position: absolute;
    top: 0; bottom: 0;
    width: 2px;
    background: var(--gold);
    box-shadow: 1px 0 0 var(--gold-deep);
  }
  .panel__divider--left { left: 210px; }
  .panel__divider--right { left: 730px; }
  .jackpot-title {
    position: absolute;
    left: 0; right: 0; top: 326px;
    margin: 0;
    text-align: center;
    font-family: "Bowlby One", "Arial Black", sans-serif;
    font-size: 50px;
    font-weight: 400;
    line-height: 52px;
  }
  .jackpot-title__text {
    display: inline-block;
    transform: scaleX(1.22);
    letter-spacing: 1px;
    color: var(--gold);
    background: linear-gradient(180deg, var(--gold-light) 0%, #ffe36a 42%, var(--gold) 55%, var(--gold-deep) 100%);
    -webkit-background-clip: text;
    background-clip: text;
    -webkit-text-fill-color: transparent;
    -webkit-text-stroke: 2px #140d00;
    filter: drop-shadow(0 2px 0 #000) drop-shadow(0 0 3px rgba(255,255,255,0.6));
  }
  .ticker-band {
    position: absolute;
    left: 0; top: 618px;
    width: 1200px; height: 38px;
    background: rgba(2,26,5,0.92);
  }
</style>
</head>
<body>
  <main class="stage">
    <div class="panel-glow"></div>
    <div class="title-glow"></div>
    <div class="star-burst star-burst--left" role="img" aria-label="Burst of glossy pale stars with gold light rays"></div>
    <div class="star-burst star-burst--right" role="img" aria-label="Burst of glossy pale stars with gold light rays"></div>

    <div class="panel panel--title-tab"></div>
    <div class="panel panel--main"></div>

    <h1 class="jackpot-title"><span class="jackpot-title__text">JACKPOT</span></h1>

    <div class="panel panel--detail-tab"></div>
    <div class="panel panel--detail">
      <span class="panel__divider panel__divider--left"></span>
      <span class="panel__divider panel__divider--right"></span>
    </div>

    <div class="ticker-band"></div>
  </main>
</body>
</html>
```